Medical device box for kits used for self testing purposes. Attractive simplistic design

Looking for a design that will go on a box that offer multiple range of medical testing ranging from hormones panel to diabetes and thyroid hormones. looking for something attractive and simple to go on a box 6 x 4.5 x 1 inches. attached are some examples from competitors. and our logo that be incorporated with the design.
Picture of the boxes have been attached, pick the color you think goes best with your design.

Target Market(s)

Patients and regular consumers

Industry/Entity Type

Medical

Requirements
Nice to have
• Simple design that is eye catching

```html
<!DOCTYPE html>
<html lang="en">
<head>
<meta charset="utf-8">
<title>Velora Hormones Panel Testing Kit – Box Lid</title>
<link rel="stylesheet" href="https://fonts.googleapis.com/css2?family=Montserrat:wght@400;600;700&display=swap">
<style>
  :root {
    --stage: #dcdcdc;
    --lid: #f6f5ef;
    --navy: #1b1b3d;
    --yellow: #f2d40c;
    --grey-text: #2e2e3a;
  }
  html, body {
    margin: 0;
    padding: 0;
    width: 784px;
    height: 1200px;
    overflow: hidden;
    background: var(--stage);
  }
  .canvas {
    position: relative;
    width: 784px;
    height: 1200px;
  }
  .box-lid {
    position: absolute;
    left: 32px;
    top: 320px;
    width: 720px;
    height: 560px;
    box-shadow: 0 10px 30px rgba(0,0,0,0.12);
  }
  .box-lid__art {
    position: absolute;
    inset: 0;
    display: block;
  }
  .brand {
    position: absolute;
    left: 0;
    right: 0;
    top: 146px;
    display: flex;
    justify-content: center;
    align-items: center;
    gap: 22px;
  }
  .brand__dot {
    width: 92px;
    height: 92px;
    border-radius: 50%;
    background: var(--yellow);
  }
  .brand__name {
    font-family: 'Montserrat', sans-serif;
    font-weight: 700;
    font-size: 104px;
    line-height: 1;
    color: var(--navy);
    letter-spacing: 1px;
  }
  .product-title {
    position: absolute;
    left: 0;
    right: 0;
    top: 379px;
    margin: 0;
    text-align: center;
    font-family: 'Montserrat', sans-serif;
    font-weight: 600;
    font-size: 31px;
    line-height: 38px;
    letter-spacing: 0.5px;
    color: var(--navy);
  }
  .product-subtitle {
    position: absolute;
    left: 0;
    right: 0;
    top: 423px;
    margin: 0;
    text-align: center;
    font-family: 'Montserrat', sans-serif;
    font-weight: 400;
    font-size: 18px;
    line-height: 22px;
    color: var(--grey-text);
  }
  .website {
    position: absolute;
    left: 0;
    right: 0;
    top: 508px;
    margin: 0;
    text-align: center;
    font-family: 'Montserrat', sans-serif;
    font-weight: 400;
    font-size: 15.5px;
    line-height: 20px;
    color: var(--grey-text);
  }
</style>
</head>
<body>
<main class="canvas">
  <section class="box-lid">
    <svg class="box-lid__art" width="720" height="560" viewBox="0 0 720 560" xmlns="http://www.w3.org/2000/svg">
      <rect class="lid-surface" x="0" y="0" width="720" height="560" fill="var(--lid)" role="img" aria-label="Faint molecule pattern across the white lid"/>
      <rect class="title-band" x="0" y="345" width="720" height="133" fill="var(--yellow)"/>
      <line x1="0" y1="345" x2="720" y2="345" stroke="var(--navy)" stroke-width="5"/>
      <line x1="0" y1="478" x2="720" y2="478" stroke="var(--navy)" stroke-width="5"/>
    </svg>

    <div class="brand">
      <span class="brand__dot"></span>
      <span class="brand__name">Velora</span>
    </div>

    <h1 class="product-title">HORMONES PANEL TESTING KIT</h1>
    <p class="product-subtitle">For Diabetes and Thyroid Hormones</p>
    <p class="website">www.websiteaddress.com</p>
  </section>
</main>
</body>
</html>
```